Make the invisible visible.... and attractive

I have an online course at http://www.brightpathlessons.example/Begin-today.html. I need an attractive graphic to sell the product. The course is a series of video, audio and handout materials set out in 32 lessons and has a free one year confidence course as a bonus.

Target Market(s)

Individuals who have problems with fear or anxiety.

Industry/Entity Type

Audio

```html
<!DOCTYPE html>
<html lang="en">
<head>
<meta charset="utf-8">
<title>Bright Path Course Online – 32 Lessons</title>
<link rel="stylesheet" href="https://fonts.googleapis.com/css2?family=Oswald:wght@300;400;500&family=Open+Sans:wght@400&family=Cabin:wght@600;700&display=swap">
<style>
  :root {
    --olive: #3e4b2b;
    --olive-soft: #4b5736;
    --panel: rgba(214, 220, 204, 0.72);
    --room-light: #f4f4f2;
    --room-mid: #e2e2de;
    --room-warm: #d9c8aa;
    --red-deep: #7d221d;
    --red: #9a2e27;
    --red-light: #b9463c;
    --white: #ffffff;
    --button-face: #f3f2ee;
    --button-edge: #c9c6bd;
  }
  * { margin: 0; padding: 0; box-sizing: border-box; }
  html, body { width: 1200px; height: 666px; overflow: hidden; background: var(--white); }

  .banner {
    position: relative;
    width: 1200px;
    height: 666px;
    overflow: hidden;
  }

  .scene-photo {
    position: absolute;
    inset: 0;
    background:
      radial-gradient(ellipse 260px 300px at 900px 330px, var(--room-warm) 0%, rgba(217,200,170,0.35) 55%, rgba(217,200,170,0) 100%),
      linear-gradient(180deg, var(--room-light) 0%, var(--room-mid) 60%, #d6d6d2 100%);
  }

  .headline-panel {
    position: absolute;
    left: 0;
    top: 37px;
    width: 438px;
    height: 296px;
    background: var(--panel);
    font-family: "Oswald", "Arial Narrow", sans-serif;
    color: var(--olive);
    text-transform: uppercase;
  }
  .headline-panel span { position: absolute; white-space: nowrap; line-height: 1; }
  .headline-online  { left: 26px;  top: 14px;  font-size: 84px; font-weight: 500; letter-spacing: 1px; }
  .headline-course  { left: 212px; top: 98px;  font-size: 48px; font-weight: 400; }
  .headline-lessons { left: 66px;  top: 148px; font-size: 50px; font-weight: 300; }
  .headline-media   { left: 108px; top: 198px; font-size: 38px; font-weight: 300; color: var(--olive-soft); }
  .headline-handout { left: 78px;  top: 240px; font-size: 38px; font-weight: 300; color: var(--olive-soft); }

  .red-wave {
    position: absolute;
    left: 0;
    top: 0;
    width: 1200px;
    height: 666px;
  }

  .bonus-seal {
    position: absolute;
    left: 494px;
    top: -10px;
    width: 252px;
    height: 232px;
  }
  .bonus-seal svg { position: absolute; inset: 0; }
  .bonus-seal-text {
    position: absolute;
    inset: 0;
    text-align: center;
    font-family: "Cabin", "Trebuchet MS", sans-serif;
    color: var(--white);
    text-transform: uppercase;
  }
  .bonus-free  { display: block; margin-top: 40px; font-size: 64px; font-weight: 700; line-height: 1; letter-spacing: 1px; }
  .bonus-label { display: block; font-size: 25px; font-weight: 600; line-height: 1.15; }

  .offer-copy {
    position: absolute;
    left: 27px;
    top: 514px;
    width: 840px;
    font-family: "Open Sans", Arial, sans-serif;
    font-size: 19.5px;
    line-height: 32.5px;
    color: var(--white);
  }

  .start-button {
    position: absolute;
    left: 897px;
    top: 468px;
    width: 288px;
    height: 180px;
    border-radius: 34px;
    background: linear-gradient(180deg, #ffffff 0%, var(--button-face) 55%, #dddad2 100%);
    border: 3px solid var(--button-edge);
    box-shadow: 0 4px 10px rgba(0,0,0,0.35), inset 0 2px 0 #ffffff;
    text-align: center;
    font-family: "Oswald", "Arial Narrow", sans-serif;
    color: var(--olive);
    text-transform: uppercase;
  }
  .start-main { display: block; margin-top: 16px; font-size: 74px; font-weight: 500; line-height: 1; }
  .start-sub  { display: block; font-size: 40px; font-weight: 500; line-height: 1.05; }
  .start-note { display: block; font-size: 17px; font-weight: 400; line-height: 1.3; letter-spacing: 0.5px; }
</style>
</head>
<body>
<main class="banner">
  <div class="scene-photo" role="img" aria-label="Photograph of a smiling man in a light T-shirt working on a laptop in a bright white living room"></div>

  <div class="headline-panel">
    <span class="headline-online">Online</span>
    <span class="headline-course">Course</span>
    <span class="headline-lessons">32 Lessons</span>
    <span class="headline-media">Video, Audio</span>
    <span class="headline-handout">and Handouts</span>
  </div>

  <svg class="red-wave" viewBox="0 0 1200 666" aria-hidden="true">
    <defs>
      <linearGradient id="waveFill" x1="0" y1="0" x2="0" y2="1">
        <stop offset="0" stop-color="#a3332b"/>
        <stop offset="1" stop-color="#7a201b"/>
      </linearGradient>
    </defs>
    <path d="M0 350 C 260 400, 520 470, 800 440 C 980 420, 1110 380, 1200 352 L1200 666 L0 666 Z" fill="#c45a4f" opacity="0.55"/>
    <path d="M0 368 C 260 420, 540 490, 820 460 C 990 442, 1110 405, 1200 378 L1200 666 L0 666 Z" fill="url(#waveFill)"/>
    <path d="M0 392 C 300 450, 580 505, 860 478 C 1010 463, 1120 430, 1200 408" fill="none" stroke="#ffffff" stroke-width="2" opacity="0.55"/>
    <path d="M0 420 C 320 480, 620 520, 900 500 C 1040 490, 1130 465, 1200 445" fill="none" stroke="#c9574b" stroke-width="3" opacity="0.6"/>
  </svg>

  <div class="bonus-seal">
    <svg viewBox="0 0 252 232" aria-hidden="true">
      <defs>
        <radialGradient id="sealFill" cx="0.45" cy="0.4" r="0.65">
          <stop offset="0" stop-color="#c0453b"/>
          <stop offset="0.7" stop-color="#9a2c25"/>
          <stop offset="1" stop-color="#6e1c18"/>
        </radialGradient>
      </defs>
      <ellipse cx="126" cy="116" rx="124" ry="112" fill="#8a2520"/>
      <ellipse cx="126" cy="114" rx="110" ry="98" fill="url(#sealFill)"/>
      <ellipse cx="126" cy="114" rx="110" ry="98" fill="none" stroke="#6e1c18" stroke-width="3"/>
    </svg>
    <div class="bonus-seal-text">
      <span class="bonus-free">Free</span>
      <span class="bonus-label">Bonus</span>
      <span class="bonus-label">Courseas</span>
    </div>
  </div>

  <p class="offer-copy">Develop powerful emotional resilience quickly and easily. The Bright Path Course Online gives you everything you need to be calm and composed in any situation. Start right now. By the end of today you will have everything you need to return you to a calm and composed state, easily.</p>

  <div class="start-button">
    <span class="start-main">Start</span>
    <span class="start-sub">Right Now</span>
    <span class="start-note">By the end of today...</span>
  </div>
</main>
</body>
</html>
```